winery and bed & breakfast business card

need a business card design
font and style same as our marketing material
also need something for letterhead

not too colorful, we want professional and simple
name
address
phone number
web site
email
Corvaletti Vineyard believes raising a family, living and working passionately with wine on the East End is a privilege. They consider the greatest accolades received over the years have been the thousands of satisfied tasting room visitors. Enlightening visitors to their products and wine region are the most important reasons they continue to make wine on the North Fork
We have created a casual and cozy environment within a rustic historic barn.
An outside seating area nestled among the vines provides visitors with unforgettable sunset views as they enjoy Corvaletti’s quality crafted wines.

Target Market(s)

adults over 21

Font styles to use
Serif

Colors
6b449b
ffc214
f78f20
ffffff

Requirements
Must have
• logo
• same font as attached
• logo colors

```html
<!DOCTYPE html>
<html lang="en">
<head>
<meta charset="utf-8">
<title>Corvaletti Vineyard – Stationery</title>
<link rel="stylesheet" href="https://fonts.googleapis.com/css2?family=Marcellus&family=Quicksand:wght@400;500&display=swap">
<style>
  :root{
    --plum:#4e3354;
    --orange:#f29224;
    --paper:#ffffff;
    --ink:#4a3a4e;
    --shadow:0 2px 5px rgba(0,0,0,.35);
  }
  *{box-sizing:border-box;margin:0;padding:0}
  html,body{width:1200px;height:1080px;overflow:hidden;background:var(--paper)}
  body{position:relative;font-family:"Quicksand",sans-serif;color:var(--ink)}
  .sheet{position:absolute;background:var(--paper);box-shadow:var(--shadow);overflow:hidden}
  .wave{position:absolute;left:0;top:0;width:100%;height:100%}

  .brand{position:absolute;display:flex;flex-direction:column;align-items:center;font-family:"Marcellus",serif;color:var(--plum);white-space:nowrap}
  .brand-dot{border-radius:50%;background:var(--orange);flex:none}
  .brand-name{display:flex;flex-direction:column;align-items:center;line-height:1}
  .brand-name .main{letter-spacing:.14em}
  .brand-name .sub{letter-spacing:.22em}

  /* business card front */
  .card-front{left:286px;top:17px;width:276px;height:158px}
  .card-front .brand{left:8px;top:15px;width:112px}
  .card-front .brand-dot{width:44px;height:44px;margin-bottom:7px}
  .card-front .main{font-size:12.5px}
  .card-front .sub{font-size:5.5px;margin-top:2px}
  .holder{position:absolute;left:145px;top:34px;color:var(--plum);white-space:nowrap}
  .holder-name{font-family:"Marcellus",serif;font-size:11.5px}
  .holder-role{font-size:8px;margin-top:3px}
  .card-contact{position:absolute;font-size:8px;color:var(--plum);line-height:1.1;white-space:nowrap}
  .card-contact li{list-style:none;display:flex;align-items:flex-start;gap:4px;margin-bottom:1px}
  .card-contact svg{width:8px;height:8px;flex:none;margin-top:1px}
  .card-contact.left{left:12px;top:124px}
  .card-contact.right{left:142px;top:124px}
  .card-contact.right li{margin-bottom:6px}

  /* business card back */
  .card-back{left:602px;top:20px;width:276px;height:158px}
  .card-back .brand{left:50%;top:50%;transform:translate(-50%,-50%)}
  .card-back .main{font-size:20px}
  .card-back .sub{font-size:8px;margin-top:3px}

  /* letterhead */
  .letterhead{left:257px;top:205px;width:671px;height:867px}
  .letterhead .brand{left:34px;top:40px;width:156px}
  .letterhead .brand-dot{width:72px;height:72px;margin-bottom:10px}
  .letterhead .main{font-size:20px}
  .letterhead .sub{font-size:9px;margin-top:4px}
  .lh-contact{position:absolute;font-size:14px;line-height:1;white-space:nowrap}
  .lh-contact li{list-style:none;display:flex;align-items:center;gap:9px;margin-bottom:9px}
  .lh-contact svg{width:18px;height:18px;flex:none}
  .lh-contact.left{left:40px;top:778px;color:var(--ink)}
  .lh-contact.right{left:440px;top:815px;color:var(--plum)}
</style>
</head>
<body>

<section class="sheet card-front" aria-label="Business card front">
  <svg class="wave" viewBox="0 0 276 158" preserveAspectRatio="none" aria-hidden="true">
    <path d="M0 104 C90 116 180 80 276 82 L276 158 L0 158Z" fill="var(--plum)"/>
    <path d="M0 113 C90 124 180 90 276 92 L276 158 L0 158Z" fill="var(--paper)"/>
    <path d="M0 116 C90 127 180 93 276 95 L276 158 L0 158Z" fill="var(--orange)"/>
  </svg>
  <div class="brand">
    <span class="brand-dot"></span>
    <span class="brand-name"><span class="main">CORVALETTI</span><span class="sub">VINEYARD</span></span>
  </div>
  <div class="holder">
    <p class="holder-name">LUCA CORVALETTI</p>
    <p class="holder-role">Owner-Winemaker</p>
  </div>
  <ul class="card-contact left">
    <li><svg viewBox="0 0 10 10"><path d="M1 5 L5 1 L9 5 H8 V9 H2 V5Z" fill="var(--plum)"/></svg><span>482 Orchard Lane,<br>Cutchogue, NY 11935</span></li>
    <li><svg viewBox="0 0 10 10"><rect x="3" y="1" width="4" height="8" rx="1" fill="var(--plum)"/></svg><span>631-555-0147</span></li>
  </ul>
  <ul class="card-contact right">
    <li><svg viewBox="0 0 10 10"><circle cx="5" cy="5" r="4" fill="none" stroke="var(--plum)" stroke-width="1.2"/><path d="M1 5H9M5 1V9" stroke="var(--plum)"/></svg><span>www.corvalettivineyard.com</span></li>
    <li><svg viewBox="0 0 10 10"><rect x="1" y="2" width="8" height="6" fill="none" stroke="var(--plum)" stroke-width="1.2"/><path d="M1 2L5 6L9 2" fill="none" stroke="var(--plum)"/></svg><span>info@corvalettivineyard.com</span></li>
  </ul>
</section>

<section class="sheet card-back" aria-label="Business card back">
  <div class="brand">
    <span class="brand-name"><span class="main">CORVALETTI</span><span class="sub">VINEYARD</span></span>
  </div>
</section>

<section class="sheet letterhead" aria-label="Letterhead">
  <svg class="wave" viewBox="0 0 671 867" preserveAspectRatio="none" aria-hidden="true">
    <path d="M0 826 C120 885 380 790 671 757 L671 867 L0 867Z" fill="var(--plum)"/>
    <path d="M0 846 C140 900 400 808 671 778 L671 867 L0 867Z" fill="var(--paper)"/>
    <path d="M120 867 C320 860 470 815 671 786 L671 867Z" fill="var(--orange)"/>
  </svg>
  <div class="brand">
    <span class="brand-dot"></span>
    <span class="brand-name"><span class="main">CORVALETTI</span><span class="sub">VINEYARD</span></span>
  </div>
  <ul class="lh-contact left">
    <li><svg viewBox="0 0 20 20"><path d="M2 10 L10 2 L18 10 M4 8 V18 H16 V8" fill="none" stroke="var(--orange)" stroke-width="2"/><rect x="8" y="12" width="4" height="6" fill="var(--orange)"/></svg><span>482 Orchard Lane, Cutchogue, NY 11935</span></li>
    <li><svg viewBox="0 0 20 20"><rect x="5" y="1" width="10" height="18" rx="2" fill="none" stroke="var(--orange)" stroke-width="2"/><rect x="7" y="4" width="6" height="6" fill="var(--orange)"/></svg><span>631-555-0147</span></li>
  </ul>
  <ul class="lh-contact right">
    <li><svg viewBox="0 0 20 20"><circle cx="10" cy="10" r="8" fill="none" stroke="var(--plum)" stroke-width="2"/><path d="M2 10H18M10 2C6 6 6 14 10 18M10 2C14 6 14 14 10 18" fill="none" stroke="var(--plum)" stroke-width="1.5"/></svg><span>www.corvalettivineyard.com</span></li>
    <li><svg viewBox="0 0 20 20"><rect x="1" y="4" width="18" height="12" fill="none" stroke="var(--plum)" stroke-width="2"/><path d="M1 4L10 11L19 4" fill="none" stroke="var(--plum)" stroke-width="1.5"/></svg><span>info@corvalettivineyard.com</span></li>
  </ul>
</section>

</body>
</html>
```